Bluebonnet Greenworks Summit needs a marketing flyer

We need a full page graphic for our upcoming Forum that can also be converted into a website "header" for social media, etc.: "Bluebonnet Greenworks Summit - Shaping Change Across the Constructed World"

INTRODUCTION:
During the first week of August 2022, Q-MarTV is presenting the Bluebonnet Greenworks Summit - Shaping Change Across the Constructed World.

One of the most exciting aspects of this conference will be the bringing together of multiple organizations including for-profits and nonprofits, K-12’s and higher education, cities and counties and other governmental agencies, as well as architects, engineers, and contractors to collaboratively present and discuss issues and ideas related to sustainability, with a Texas focus.

This event will be a catalyst for public and private project owners to holistically gather information and momentum as we bring the resources and vision needed to achieve the goal of zero carbon emissions from the built environment by 2040, and address water, green space and the natural environment, transportation, equity, and funding, among other topics.

```html
<!DOCTYPE html>
<html lang="en">
<head>
<meta charset="utf-8">
<title>Bluebonnet Greenworks Summit – Flyer</title>
<link href="https://fonts.googleapis.com/css2?family=Montserrat:wght@300;400;700;800&display=swap" rel="stylesheet">
<style>
  :root {
    --royal-blue: #1c3f94;
    --leaf-green: #8bb63a;
    --white: #ffffff;
    --paper-bg: #e9e9e6;
    --forest-dark: #2f5a25;
    --forest-light: #a9d06a;
    --soil: #4a3424;
  }
  * { margin: 0; padding: 0; box-sizing: border-box; }
  html, body { width: 1200px; height: 1200px; overflow: hidden; }
  body {
    background: var(--paper-bg);
    font-family: "Montserrat", sans-serif;
    position: relative;
  }
  .flyer {
    position: absolute;
    left: 190px; top: 20px;
    width: 820px; height: 1160px;
    background: var(--white);
    overflow: hidden;
  }
  .flyer-art { position: absolute; inset: 0; }
  .brand-name {
    position: absolute;
    left: 44px; top: 44px;
    font-weight: 700; font-size: 26px; color: var(--white);
    letter-spacing: 2px; text-transform: uppercase;
  }
  .content {
    position: absolute;
    left: 90px; top: 560px; width: 640px;
    text-align: center; color: var(--white);
  }
  .intro {
    font-weight: 800; font-size: 19px; line-height: 1.25;
    text-transform: uppercase; letter-spacing: 0.5px;
  }
  .intro .accent { color: var(--leaf-green); }
  .title {
    margin-top: 14px;
    font-weight: 800; font-size: 50px; line-height: 1.02;
    color: var(--leaf-green); text-transform: uppercase;
  }
  .subtitle {
    margin-top: 8px;
    font-weight: 700; font-size: 18px; letter-spacing: 0.6px;
    text-transform: uppercase;
  }
  .divider {
    width: 110px; height: 3px; background: var(--leaf-green);
    margin: 22px auto 24px;
  }
  .body-copy {
    font-weight: 300; font-size: 14px; line-height: 1.6;
    text-align: justify; text-align-last: center;
    margin: 0 20px 16px;
  }
  .body-copy strong { font-weight: 800; }
  .web-address {
    position: absolute;
    left: 290px; top: 1100px; width: 460px;
    text-align: center; white-space: nowrap;
    font-weight: 800; font-size: 28px; color: var(--royal-blue);
  }
</style>
</head>
<body>
  <main class="flyer">
    <svg class="flyer-art" viewBox="0 0 820 1160" width="820" height="1160">
      <defs>
        <linearGradient id="photo-tones" x1="0" y1="0" x2="0" y2="1">
          <stop offset="0" stop-color="var(--forest-light)"/>
          <stop offset="0.45" stop-color="var(--forest-dark)"/>
          <stop offset="1" stop-color="var(--soil)"/>
        </linearGradient>
      </defs>
      <rect class="hero-photo" x="0" y="0" width="820" height="760" fill="url(#photo-tones)"
            role="img" aria-label="Photo of a hand holding seedlings growing from soil on stacked coins, forest background"/>
      <path class="arc-rule" d="M0,700 C180,500 500,400 820,420" fill="none" stroke="var(--leaf-green)" stroke-width="12"/>
      <path class="blue-panel" d="M0,722 C180,522 500,422 820,442 L820,1160 L0,1160 Z" fill="var(--royal-blue)"/>
      <path class="corner-left" d="M0,960 C90,1060 170,1120 260,1160 L0,1160 Z" fill="var(--white)"/>
      <path class="corner-right" d="M820,840 C780,960 740,1060 700,1160 L820,1160 Z" fill="var(--white)"/>
      <ellipse class="footer-arc" cx="520" cy="1230" rx="340" ry="170" fill="var(--leaf-green)"/>
    </svg>

    <p class="brand-name">Q-MarTV</p>

    <section class="content">
      <p class="intro">During the first week of <span class="accent">August 2022</span><br>Q-MarTV is presenting the</p>
      <h1 class="title">Bluebonnet<br>Greenworks Summit</h1>
      <p class="subtitle">Shaping Change Across the Constructed World</p>
      <div class="divider"></div>
      <p class="body-copy">One of the most exciting aspects of this conference will be the bringing together of multiple organizations including for-profits and nonprofits, K-12’s and higher education, cities and counties and other governmental agencies, as well as architects, engineers, and contractors to collaboratively <strong>present and discuss issues and ideas related to sustainability,</strong> with a Texas focus.</p>
      <p class="body-copy">This event will be a catalyst for public and private project owners to holistically gather information and momentum as we bring the resources and vision needed to achieve <strong>the goal of zero carbon emissions from the built environment by 2040,</strong> and address water, green space and the natural environment, transportation, equity, and funding, among other topics.</p>
    </section>

    <p class="web-address">www.qmartv-summit.org</p>
  </main>
</body>
</html>
```